HARBORLINE MAILWORKS - DIRECT MAIL BUSINESS CARD

Harborline Mailworks, 418 E Birch Ave, Briarton NE 73512 405-287-9046 email - dalew412@mailnest.example Owner Dale Wren Serving customers since 1989, Product - Direct mail marketing

Target Market(s)

Businesses,churches and non-profits

Industry/Entity Type

Marketing

Contact Beacon for Business Card

Dark blue UV coated card with white letters on front. Maybe add a sketch of a mail addressing machine. On the back either Dark blue or full color with the sketch of a postman throwing a letter towards a world globe, with the phrase reach your world. Or the postman throwing a letter towards a archery target with the phrase, reach your target market.

Font styles to use
Serif

Colors
0355a3

Requirements
Must have
• BEACON HARBORLINE MAILWORKS
• 418 E BIRCH AVE
• BRIARTON NE 73512
• 405-287-9046
• dalew412@mailnest.example
• DALE WREN, OWNER
• DIRECT MAIL MARKETING
Nice to have
• SERVING CUSTOMERS SINCE 1989 SKETCH OF MAIL ADDRESSING EQUIPMENT, IN THE BACKGROUND, ON THE FRONT
• ON THE BACK, SKETCH OF POSTMAN THROWING LETTER TO THE WORLD
• GLOBE, WITH THE PHRASE, REACH YOUR WORLD, OR THE LETTER TO A TARGET, WITH PHRASE, REACH YOUR TARGET MARKET
Should not have
• PHOTOS OR FLOWERS

```html
<!DOCTYPE html>
<html lang="en">
<head>
<meta charset="utf-8">
<title>Beacon Harborline Mailworks – Business Card</title>
<link rel="stylesheet" href="https://fonts.googleapis.com/css2?family=Montserrat:wght@700&family=Open+Sans:wght@300;400;600;700&display=swap">
<style>
  :root {
    --backdrop: #2b2b2d;
    --card-blue: #2a3a8c;
    --card-blue-deep: #23317a;
    --ink-white: #ffffff;
    --rule: rgba(255,255,255,0.75);
    --globe-faint: rgba(255,255,255,0.08);
  }
  * { margin: 0; padding: 0; box-sizing: border-box; }
  html, body {
    width: 1200px; height: 900px; overflow: hidden;
    background: var(--backdrop);
  }
  .canvas { position: relative; width: 1200px; height: 900px; }
  .card {
    position: absolute; left: 250px; width: 700px; height: 400px;
    border-radius: 26px;
    background: linear-gradient(160deg, var(--card-blue) 0%, var(--card-blue-deep) 100%);
    color: var(--ink-white);
    font-family: "Open Sans", sans-serif;
    overflow: hidden;
  }
  .card--front { top: 30px; }
  .card--back { top: 470px; }

  .mascot-art {
    position: absolute; left: 50%; transform: translateX(-50%);
    border-radius: 60px;
    background: linear-gradient(90deg, rgba(255,255,255,0.85), rgba(255,255,255,0.95));
  }
  .card--front .mascot-art { top: 45px; width: 260px; height: 140px; }
  .card--back .mascot-art { top: 30px; width: 200px; height: 108px; }

  .globe-backdrop {
    position: absolute; left: -150px; top: 60px; width: 420px; height: 420px;
    border-radius: 50%; background: var(--globe-faint);
  }

  .brand-name {
    position: absolute; left: 0; right: 0; text-align: center;
    font-family: "Montserrat", sans-serif; font-weight: 700;
    letter-spacing: 0.2px;
  }
  .card--front .brand-name { top: 210px; font-size: 21px; }
  .card--back .brand-name { top: 146px; font-size: 16px; }

  .rule {
    position: absolute; left: 90px; right: 90px; height: 1px;
    background: linear-gradient(90deg, rgba(255,255,255,0) 0%, var(--rule) 50%, rgba(255,255,255,0) 100%);
  }

  .tagline {
    position: absolute; top: 282px; left: 0; right: 0; text-align: center;
    font-weight: 300; font-size: 19px; letter-spacing: 1.5px;
  }

  .owner-name {
    position: absolute; top: 178px; left: 0; right: 0; text-align: center;
    font-family: "Montserrat", sans-serif; font-weight: 700; font-size: 30px;
    letter-spacing: 0.5px;
  }
  .owner-title {
    position: absolute; top: 216px; left: 0; right: 0; text-align: center;
    font-size: 13px; letter-spacing: 1px;
  }

  .contact {
    position: absolute; top: 252px; left: 0; right: 0;
    display: flex; justify-content: center; gap: 22px;
    font-size: 16px; line-height: 26px;
  }
  .contact__lines { text-align: right; }
  .contact__line { display: flex; align-items: center; justify-content: flex-end; gap: 8px; }
  .contact__address { text-align: left; font-size: 15px; letter-spacing: 0.5px; }
  .icon { width: 13px; height: 13px; fill: none; stroke: var(--ink-white); stroke-width: 1.6; }

  .service {
    position: absolute; top: 344px; left: 0; right: 0; text-align: center;
    font-size: 16px; letter-spacing: 1px;
  }
</style>
</head>
<body>
<main class="canvas">

  <section class="card card--front">
    <div class="mascot-art" role="img" aria-label="Illustration of a running postman tossing a letter toward a world globe"></div>
    <div class="brand-name">BEACON HARBORLINE MAILWORKS</div>
    <div class="rule" style="top:258px"></div>
    <div class="tagline">SERVING CUSTOMERS SINCE 1989</div>
    <div class="rule" style="top:340px"></div>
  </section>

  <section class="card card--back">
    <div class="globe-backdrop" role="img" aria-label="Faint large world globe decoration"></div>
    <div class="mascot-art" role="img" aria-label="Illustration of a running postman tossing a letter toward a world globe"></div>
    <div class="brand-name">BEACON HARBORLINE MAILWORKS</div>
    <div class="owner-name">DALE WREN</div>
    <div class="owner-title">OWNER</div>
    <div class="contact">
      <div class="contact__lines">
        <div class="contact__line">405-287-9046
          <svg class="icon" viewBox="0 0 16 16"><path d="M4 1.5 L6.5 5 L5 6.5 C6 8.5 7.5 10 9.5 11 L11 9.5 L14.5 12 L13 14.5 C7 14 2 9 1.5 3 Z"/></svg>
        </div>
        <div class="contact__line">dalew412@mailnest.example
          <svg class="icon" viewBox="0 0 16 16"><rect x="1.5" y="3.5" width="13" height="9" rx="1"/><path d="M1.5 4 L8 9 L14.5 4"/></svg>
        </div>
      </div>
      <div class="contact__address">418 E BIRCH AVE<br>BRIARTON NE 73512</div>
    </div>
    <div class="rule" style="top:330px"></div>
    <div class="service">DIRECT MAIL MARKETING</div>
  </section>

</main>
</body>
</html>
```